VELUNDORA Multistep design - needs to match our existing design.

We have a multistep form(7 pages) we need the design for (rest of the website is done).
The multistep form is a vital part of the website, as it is the main service - so the form design should fit into the rest of the site.
Please take a look at the attached file - all about colors, fonts etc. is included in the file.

Target Market(s)

People looking for an interior architect in Denmark

Industry/Entity Type

Interior Design

Number of Pages Required

1 page

Requirements
Nice to have
• It's attached in the pdf file

```html
<!DOCTYPE html>
<html lang="en">
<head>
<meta charset="utf-8">
<title>VELUNDORA – Choose your options</title>
<link href="https://fonts.googleapis.com/css2?family=Raleway:wght@400;500&display=swap" rel="stylesheet">
<style>
  :root {
    --page-bg: #f0f0f0;
    --hero-dark: #141414;
    --hero-mid: #2b2b2b;
    --hero-warm: #3a2e26;
    --nav-bg: rgba(14, 14, 16, 0.72);
    --text-light: #ffffff;
    --text-muted: #a6a6a6;
    --button-border: #9a9a9a;
    --button-solid: #050505;
  }
  * { box-sizing: border-box; margin: 0; padding: 0; }
  html, body {
    width: 1200px;
    height: 1200px;
    overflow: hidden;
    background: var(--page-bg);
    font-family: "Raleway", sans-serif;
  }
  .hero {
    position: absolute;
    left: 62px;
    top: 305px;
    width: 1079px;
    height: 591px;
    overflow: hidden;
    color: var(--text-light);
  }
  .hero-backdrop {
    position: absolute;
    inset: 0;
    background:
      radial-gradient(ellipse 45% 35% at 40% 35%, rgba(90, 40, 40, 0.35), transparent 70%),
      radial-gradient(ellipse 40% 20% at 35% 68%, rgba(110, 95, 55, 0.35), transparent 70%),
      linear-gradient(170deg, var(--hero-dark) 0%, var(--hero-mid) 50%, var(--hero-warm) 80%, var(--hero-dark) 100%);
  }
  .site-nav {
    position: absolute;
    left: 0; top: 0;
    width: 100%;
    height: 57px;
    background: var(--nav-bg);
    display: flex;
    align-items: center;
    justify-content: space-between;
    padding: 0 34px;
  }
  .brand {
    font-size: 24px;
    font-weight: 400;
    letter-spacing: 0.2px;
  }
  .nav-links {
    display: flex;
    gap: 29px;
    list-style: none;
    font-size: 13px;
  }
  .options {
    position: absolute;
    left: 0; top: 0;
    width: 100%;
    text-align: center;
  }
  .options-title {
    position: absolute;
    width: 100%;
    top: 188px;
    font-size: 26px;
    font-weight: 500;
  }
  .options-lead, .form-lead {
    position: absolute;
    width: 100%;
    font-size: 12px;
    color: var(--text-muted);
  }
  .options-lead { top: 238px; }
  .form-title {
    position: absolute;
    width: 100%;
    top: 323px;
    font-size: 18px;
    font-weight: 500;
  }
  .form-lead { top: 361px; }
  .choice-buttons {
    position: absolute;
    top: 408px;
    left: 388px;
    display: flex;
    gap: 17px;
  }
  .choice {
    width: 143px;
    height: 45px;
    border-radius: 3px;
    font-family: "Raleway", sans-serif;
    font-size: 18px;
    color: var(--text-light);
    display: flex;
    align-items: center;
    justify-content: center;
  }
  .choice-outline { border: 1px solid var(--button-border); background: transparent; }
  .choice-solid { border: 1px solid var(--button-solid); background: var(--button-solid); }
</style>
</head>
<body>
  <section class="hero">
    <div class="hero-backdrop" role="img" aria-label="Blurred, darkened photo of an architect's hand drawing plans beside a scale ruler on a wooden desk"></div>
    <header class="site-nav">
      <div class="brand">VELUNDORA</div>
      <ul class="nav-links">
        <li>The concept</li>
        <li>Private</li>
        <li>profession</li>
        <li>Architect</li>
        <li>About VELUNDORA</li>
      </ul>
    </header>
    <div class="options">
      <h1 class="options-title">Choose your options</h1>
      <p class="options-lead">There are many variations of passages of Lorem Ipsum</p>
      <h2 class="form-title">Fill in the form</h2>
      <p class="form-lead">There are many variations of passages of Lorem</p>
      <div class="choice-buttons">
        <div class="choice choice-outline">Private</div>
        <div class="choice choice-solid">Business</div>
      </div>
    </div>
  </section>
</body>
</html>
```